Tarnwickhub.com home page

On the existing home page I want to eliminate people in circles and promote these three earning opportunities:
1." Make a referral to existing advertiser"
Earn up to $5000 when you make a successful referral to one of our advertisers.
2."Sign up a new business to offer referral commisions to ambassaadors". Earn up to $5000 or more when you earn 5% of money paid out by business in referral fees.
3."Sign up new ambassadors"
Earn up to $5000 or more when you earn 5% of the money the ambassadors you sign up earn.

In each offer I want a learn more button .

Industry/Entity Type

Business

Font styles to use
Serif

```html
<!DOCTYPE html>
<html lang="en">
<head>
<meta charset="utf-8">
<title>Tarnwickhub.com – Referral Marketplace</title>
<link rel="stylesheet" href="https://fonts.googleapis.com/css2?family=Roboto:wght@400;500;700&family=Lato:wght@400;700&family=Open+Sans:wght@400;600;700&display=swap">
<style>
  :root {
    --brand-green: #2bae5e;
    --brand-green-dark: #23964f;
    --ink: #1c1c1c;
    --ink-soft: #2e2e2e;
    --grey-text: #6f7477;
    --nav-text: #555a5e;
    --white: #ffffff;
    --hero-top: #eef0f2;
  }
  * { box-sizing: border-box; margin: 0; padding: 0; }
  html, body { width: 1200px; height: 631px; overflow: hidden; background: var(--white); }
  .page { position: relative; width: 1200px; height: 631px; overflow: hidden; font-family: "Lato", sans-serif; color: var(--ink); }

  /* Header */
  .site-header { position: absolute; left: 0; top: 0; width: 1200px; height: 80px; background: var(--white); }
  .brand { position: absolute; left: 6px; top: 14px; }
  .brand-name { font-family: "Open Sans", sans-serif; font-weight: 600; font-size: 34px; line-height: 38px; color: var(--brand-green); letter-spacing: -0.5px; }
  .brand-tagline { font-family: "Open Sans", sans-serif; font-size: 11px; line-height: 12px; color: var(--grey-text); margin-left: 2px; letter-spacing: 0.4px; }
  .main-nav { position: absolute; top: 0; left: 733px; height: 80px; display: flex; font-family: "Open Sans", sans-serif; font-size: 14px; color: var(--nav-text); }
  .nav-item { height: 80px; display: flex; align-items: center; }
  .nav-item.is-active { background: var(--brand-green); color: var(--white); width: 72px; justify-content: center; }
  .nav-how { margin-left: 17px; }
  .nav-search { margin-left: 32px; }
  .nav-members { margin-left: 32px; }
  .nav-login { margin-left: 33px; }

  /* Hero */
  .hero { position: absolute; left: 0; top: 80px; width: 1200px; height: 468px; background: linear-gradient(to bottom, var(--hero-top) 0px, var(--white) 90px); }
  .hero-title { position: absolute; top: 21px; width: 100%; text-align: center; font-family: "Roboto", sans-serif; font-weight: 700; font-size: 40px; letter-spacing: 3px; color: var(--ink); line-height: 48px; }
  .hero-subtitle { position: absolute; top: 64px; width: 100%; text-align: center; font-family: "Roboto", sans-serif; font-weight: 400; font-size: 28px; color: var(--ink-soft); line-height: 34px; }
  .hero-lead { position: absolute; top: 101px; left: 251px; font-family: "Open Sans", sans-serif; font-size: 32px; line-height: 40px; color: var(--ink-soft); }
  .hero-lead .brand-inline { color: var(--brand-green); font-weight: 600; }

  .offer { position: absolute; left: 139px; width: 720px; font-size: 23px; line-height: 31px; color: var(--ink-soft); }
  .offer-1 { top: 166px; }
  .offer-2 { top: 243px; }
  .offer-3 { top: 347px; }

  .learn-more { position: absolute; left: 997px; width: 144px; height: 57px; background: var(--brand-green); color: var(--white); font-size: 25px; display: flex; align-items: center; justify-content: center; box-shadow: 3px 4px 5px rgba(0,0,0,0.35); }
  .learn-more-1 { top: 174px; }
  .learn-more-2 { top: 267px; }
  .learn-more-3 { top: 352px; }

  /* Signup band */
  .signup-band { position: absolute; left: 0; top: 548px; width: 1200px; height: 83px; background: var(--brand-green); }
  .signup-text { position: absolute; left: 0; top: 26px; font-family: "Open Sans", sans-serif; font-weight: 700; font-size: 16px; color: var(--white); }
  .signup-button { position: absolute; left: 970px; top: 15px; width: 199px; height: 50px; border: 2px solid var(--white); display: flex; align-items: center; justify-content: center; gap: 8px; color: var(--white); font-family: "Open Sans", sans-serif; font-size: 18px; }
</style>
</head>
<body>
<div class="page">
  <header class="site-header">
    <div class="brand">
      <div class="brand-name">Tarnwickhub</div>
      <div class="brand-tagline">Referral Marketplace</div>
    </div>
    <nav class="main-nav">
      <span class="nav-item is-active">Home</span>
      <span class="nav-item nav-how">How It Works</span>
      <span class="nav-item nav-search">Search</span>
      <span class="nav-item nav-members">Members</span>
      <span class="nav-item nav-login">Log In</span>
    </nav>
  </header>

  <section class="hero">
    <h1 class="hero-title">EASILY MAKE MORE MONEY</h1>
    <p class="hero-subtitle">JUST BY REFERRING YOURSELF, YOUR FRIENDS OR BUSINESS ASSOCIATES</p>
    <p class="hero-lead"><span class="brand-inline">Tarnwickhub</span> Offer these opportunities</p>

    <p class="offer offer-1">1-Make a referral to existing advertiser : Earn up to $5000 when you make a successful referral&nbsp; to one of our advertisers .</p>
    <p class="offer offer-2">2-Sign up a new business to offer referral commisions<br>to ambassaadors: Earn up to $5000 or more when you earn 5%<br>of money paid out by business in referral fees</p>
    <p class="offer offer-3">3-Sign up new ambassadors: Earn up to $5000 or more when<br>you earn 5% of the money the ambassadors you sign up earn</p>

    <a class="learn-more learn-more-1">Learn more</a>
    <a class="learn-more learn-more-2">Learn more</a>
    <a class="learn-more learn-more-3">Learn more</a>
  </section>

  <section class="signup-band">
    <p class="signup-text">Tarnwickhub, Fastest Growing Referral Marketplace. Earn income just by referring people you know.</p>
    <a class="signup-button">
      <svg width="24" height="22" viewBox="0 0 24 22" fill="none" stroke="#ffffff" stroke-width="1.8" stroke-linejoin="round">
        <rect x="1" y="9" width="5" height="11"/>
        <path d="M6 10 L10 3 Q11.5 1 12.5 3 L12 9 H21 Q23 9.5 22.5 11.5 L20.5 19 Q20 20 18.5 20 H6"/>
      </svg>
      <span>Free to Sign Up!</span>
    </a>
  </section>
</div>
</body>
</html>
```